" é uma empresa produtora de polpas de frutas congeladas, sumos naturais, e gelados artesanais. comercialisamos os produtos para pessoas individuais , lojas, restaurants e eventos. funcianamento: a materia prima (fruta) chega a fabrica, e é processeda segungo um protocolo definido pelas normas de saude e higiene. posterioremente é embalado e armazenado. os pedidos dos clientes chegam por telefone ou whatsaap e nós procedemos de acordo. fazemos entregas ou o cliente vem a loja. em junho sera aberta a loja/restaurante/gelataria fisica. todos os products são processados por nós. usamos produtos de qualidade, sem corantes e sem conservantes artificiais. "

```html
<!DOCTYPE html>
<html lang="pt">
<head>
<meta charset="utf-8">
<title>Frutos do Kwanza — Papel timbrado</title>
<link rel="stylesheet" href="https://fonts.googleapis.com/css2?family=Montserrat:wght@400;500;600;800&display=swap">
<style>
  :root {
    --red: #b5202b;
    --red-dark: #8c1820;
    --amber: #f2a516;
    --ink: #2b2b2b;
    --muted: #6e6e6e;
    --paper: #ffffff;
    --stage: #efe9df;
    --seal: rgba(60,80,150,.35);
  }
  * { box-sizing: border-box; margin: 0; padding: 0; }
  html, body { width: 1200px; height: 1200px; overflow: hidden; }
  body {
    background: var(--stage);
    font-family: "Montserrat", sans-serif;
    color: var(--ink);
    display: flex; align-items: center; justify-content: center;
  }
  .letterhead {
    position: relative;
    width: 780px; height: 1104px;
    background: var(--paper);
    box-shadow: 0 18px 50px rgba(0,0,0,.18);
    display: flex; flex-direction: column;
  }
  .letterhead__top {
    display: flex; justify-content: space-between; align-items: center;
    padding: 54px 60px 0;
  }
  .brand { display: flex; align-items: center; gap: 14px; }
  .brand__dot { width: 30px; height: 30px; border-radius: 50%; background: var(--amber); }
  .brand__name {
    font-weight: 800; font-size: 30px; line-height: 1.05; color: var(--red); width: 200px;
  }
  .tagline {
    font-weight: 600; font-size: 24px; color: var(--red); letter-spacing: 1px;
  }

  .title { text-align: center; margin-top: 70px; }
  .title__main { font-weight: 800; font-size: 30px; letter-spacing: 6px; }
  .title__sub { font-weight: 600; font-size: 14px; letter-spacing: 4px; margin-top: 8px; }
  .title__rule { width: 60px; height: 2px; background: var(--ink); margin: 16px auto 0; }

  .body { padding: 44px 60px 0; font-size: 13px; line-height: 1.75; color: var(--muted); }
  .body p + p { margin-top: 16px; }

  .closing { display: flex; justify-content: flex-end; padding: 30px 60px 0; }
  .closing__block { width: 260px; }
  .closing__label { font-size: 12px; color: var(--muted); padding-left: 110px; }
  .closing__marks { display: flex; align-items: center; gap: 16px; margin-top: 10px; }
  .seal { flex: none; width: 90px; height: 90px; border-radius: 50%; border: 4px solid var(--seal); }
  .signature { display: block; width: 150px; height: 54px; border-radius: 6px;
    background: linear-gradient(90deg, rgba(40,40,60,.08), rgba(40,40,60,.2)); }

  .footer { margin-top: auto; }
  .footer__contacts { padding: 0 60px 14px; font-size: 10px; color: var(--muted); line-height: 1.6; }
  .footer__band {
    background: var(--red); color: #fff; font-size: 11px;
    display: flex; justify-content: flex-end; gap: 30px; padding: 10px 60px;
  }
  .footer__item { display: flex; align-items: center; gap: 7px; }
  .footer__item svg { width: 14px; height: 14px; fill: #fff; }
  .footer__base {
    display: flex; align-items: center; background: var(--red-dark); color: #fff;
    font-size: 11px; height: 38px;
  }
  .footer__accent { width: 60px; height: 100%; background: var(--amber); }
  .footer__address { display: flex; align-items: center; gap: 7px; padding-left: 20px; }
  .footer__address svg { width: 14px; height: 14px; fill: var(--amber); }
</style>
</head>
<body>
  <main class="letterhead">
    <header class="letterhead__top">
      <div class="brand">
        <span class="brand__dot"></span>
        <span class="brand__name">Frutos do Kwanza</span>
      </div>
      <div class="tagline">Fruta Natural</div>
    </header>

    <section class="title">
      <h1 class="title__main">PAPER MOCKUP</h1>
      <p class="title__sub">PSD RESOURCE BY PAPELARIA AURORA</p>
      <div class="title__rule"></div>
    </section>

    <section class="body">
      <p>Lorem ipsum dolor sit amet, consectetur adipiscing elit. Donec orci purus, luctus vitae dignissim eu, iaculis sed purus. Vivamus faucibus, ipsum nec aliquet viverra, leo mauris condimentum ligula, sit amet sagittis enim ligula quis arcu. Nam egestas tortor id nisi porttitor mattis. In tortor ante, ultricies in suscipit a, tempus non massa. Vivamus et auctor ex. Fusce vel massa nulla. Phasellus nec eros mauris, et scelerisque orci.</p>
      <p>Donec malesuada orci vitae nulla accumsan porta a id metus. Quisque accumsan iaculis magna sit amet fringilla. Maecenas consequat, magna eget tincidunt semper, odio nibh rutrum mi, id feugiat ante nisl eu risus. Vestibulum nunc orci, rhoncus e placerat in, ultricies in mi. Cras mattis varius eros, vel fringilla nisi suscipit eget. Quisque scelerisque sagittis nulla at porttitor.</p>
      <p>Sed id augue vitae urna euismod commodo aliquet a quam. Pellentesque arcu velit, cursus et malesuada ut, consequat et diam. Nullam erat sem, rhoncus id ullamcorper vitae, rhoncus et arcu. In ultricies ultricies nulla, ut rutrum nisi iaculis at. Donec eu magna a metus ornare faucibus. Fusce aliquet faucibus ultricies. Morbi semper, est id tincidunt gravida, sem arcu adipiscing lacus, ac bibendum nulla leo eu purus. Quisque nec diam sed risus consectetur a cursus quis quis nibh. Vestibulum id purus lorem.</p>
    </section>

    <section class="closing">
      <div class="closing__block">
        <p class="closing__label">Sincerely,</p>
        <div class="closing__marks">
          <span class="seal"></span>
          <span class="signature" role="img" aria-label="Assinatura manuscrita"></span>
        </div>
      </div>
    </section>

    <footer class="footer">
      <div class="footer__contacts">
        <p>(+244) 923 410 552 | ola@frutosdokwanza.ao</p>
        <p>Rua das Acácias 27, Maianga, Luanda, Angola</p>
      </div>
      <div class="footer__band">
        <span class="footer__item">
          <svg viewBox="0 0 24 24"><path d="M6.6 10.8a15 15 0 0 0 6.6 6.6l2.2-2.2a1 1 0 0 1 1-.25 11.4 11.4 0 0 0 3.6.57 1 1 0 0 1 1 1V20a1 1 0 0 1-1 1A17 17 0 0 1 3 4a1 1 0 0 1 1-1h3.5a1 1 0 0 1 1 1c0 1.25.2 2.45.57 3.57a1 1 0 0 1-.25 1z"/></svg>
          (+244) 923 410 553
        </span>
        <span class="footer__item">
          <svg viewBox="0 0 24 24"><path d="M3 5h18v14H3z M3 5l9 7 9-7" fill="none" stroke="#fff" stroke-width="2"/></svg>
          pedidos@frutosdokwanza.ao
        </span>
        <span class="footer__item">
          <svg viewBox="0 0 24 24"><circle cx="12" cy="12" r="9" fill="none" stroke="#fff" stroke-width="2"/><path d="M3 12h18M12 3c3 3 3 15 0 18M12 3c-3 3-3 15 0 18" fill="none" stroke="#fff" stroke-width="1.5"/></svg>
          www.frutosdokwanza.ao
        </span>
      </div>
      <div class="footer__base">
        <span class="footer__accent"></span>
        <span class="footer__address">
          <svg viewBox="0 0 24 24"><path d="M12 2a7 7 0 0 0-7 7c0 5 7 13 7 13s7-8 7-13a7 7 0 0 0-7-7zm0 9.5A2.5 2.5 0 1 1 12 6.5a2.5 2.5 0 0 1 0 5z"/></svg>
          Av. 4 de Fevereiro 88, Luanda
        </span>
      </div>
    </footer>
  </main>
</body>
</html>
```